Business Card for a Mortgage Agent (myself)

I need a business card for my new job as Mortgage Agent. The Broker's logo is to be on the card as well as the brokerage License number. Not sure if to include a photo or not. Info to be on card.
Dante Roux
Mortgage Agent
Lic # M47105386
Cell: 905-614-2753
Email: danterouxk.ma@fennmail.com
Web: www.karlvostermortgages.com
TPW Brokerage Lic. # 73918

```html
<!DOCTYPE html>
<html lang="en">
<head>
<meta charset="utf-8">
<title>Dante Roux – Mortgage Agent Business Card</title>
<link rel="stylesheet" href="https://fonts.googleapis.com/css2?family=Jost:wght@300;400;600&family=Arimo:wght@400&display=swap">
<style>
  :root {
    --page: #efefef;
    --brand-blue: #0657a6;
    --brand-yellow: #fec80c;
    --white: #ffffff;
    --back-grey: #a9aaac;
  }
  * { margin: 0; padding: 0; box-sizing: border-box; }
  html, body { width: 1200px; height: 1000px; overflow: hidden; }
  body { background: var(--page); position: relative; font-family: "Jost", sans-serif; }

  .card { position: absolute; overflow: hidden; }
  .card--front { left: 291px; top: 123px; width: 634px; height: 363px; background: var(--brand-blue); }
  .card--back { left: 288px; top: 542px; width: 637px; height: 364px; background: var(--back-grey); }

  .front-shapes { position: absolute; inset: 0; }

  .identity { position: absolute; left: 54px; top: 40px; color: var(--white); }
  .identity__name {
    font-weight: 600; font-size: 25px; letter-spacing: 1.5px; line-height: 1;
    display: flex; align-items: center; gap: 6px;
  }
  .identity__rule { display: inline-block; width: 62px; height: 2px; background: var(--white); }
  .identity__title { font-weight: 300; font-size: 16px; letter-spacing: 3.4px; margin-top: 6px; }

  .contacts {
    position: absolute; left: 30px; top: 131px; list-style: none;
    font-family: "Arimo", sans-serif; font-size: 17px; color: var(--white);
  }
  .contacts li { display: flex; align-items: center; height: 26px; }
  .contacts li.contacts__plain { margin-top: 2px; }
  .contacts .icon { width: 14px; height: 14px; margin-right: 10px; flex: none; }
  .contacts .icon--blank { visibility: hidden; }

  .agent-licence {
    position: absolute; left: 250px; top: 307px;
    font-family: "Arimo", sans-serif; font-size: 16px; color: var(--brand-yellow);
  }

  .brokerage { position: absolute; left: 380px; top: 95px; width: 220px; text-align: center; color: var(--brand-blue); }
  .brokerage__mark { display: flex; align-items: center; justify-content: center; gap: 12px; }
  .brokerage__square { width: 34px; height: 34px; background: var(--brand-yellow); }
  .brokerage__name { font-weight: 600; font-size: 40px; letter-spacing: 10px; line-height: 1; }
  .brokerage__licence { font-family: "Arimo", sans-serif; font-size: 9px; margin-top: 12px; padding-left: 110px; }

  .back-mark {
    position: absolute; inset: 0; display: flex; align-items: center; justify-content: center; gap: 18px;
    color: var(--white);
  }
  .back-mark__square { width: 46px; height: 46px; background: var(--white); }
  .back-mark__name { font-weight: 600; font-size: 64px; letter-spacing: 14px; line-height: 1; }
</style>
</head>
<body>

<section class="card card--front" aria-label="Business card front">
  <svg class="front-shapes" width="634" height="363" viewBox="0 0 634 363" aria-hidden="true">
    <polygon points="171,305 500,305 500,329 183,329" fill="var(--white)"/>
    <path d="M370,0 C316,45 312,160 372,222 C440,292 540,342 634,363 L634,0 Z" fill="var(--brand-yellow)"/>
    <path d="M372,0 C322,40 318,130 366,188 C430,262 540,314 634,334 L634,0 Z" fill="var(--white)"/>
  </svg>

  <div class="identity">
    <h1 class="identity__name">DANTE ROUX <span class="identity__rule"></span></h1>
    <p class="identity__title">MORTGAGE AGENT</p>
  </div>

  <ul class="contacts">
    <li>
      <svg class="icon" viewBox="0 0 24 24"><path fill="#fff" d="M6.6 10.8a15 15 0 0 0 6.6 6.6l2.2-2.2c.3-.3.7-.4 1-.2 1.1.4 2.3.6 3.6.6.6 0 1 .4 1 1V20c0 .6-.4 1-1 1A17 17 0 0 1 3 4c0-.6.4-1 1-1h3.5c.6 0 1 .4 1 1 0 1.3.2 2.5.6 3.6.1.3 0 .7-.2 1z"/></svg>
      905-614-2753
    </li>
    <li>
      <svg class="icon" viewBox="0 0 24 24"><rect x="2" y="5" width="20" height="14" fill="#fff"/><path d="M2 5l10 8 10-8" fill="none" stroke="var(--brand-blue)" stroke-width="2"/></svg>
      danterouxk.ma@fennmail.com
    </li>
    <li>
      <svg class="icon" viewBox="0 0 24 24"><circle cx="12" cy="12" r="10" fill="#fff"/><g fill="none" stroke="var(--brand-blue)" stroke-width="1.6"><ellipse cx="12" cy="12" rx="4" ry="10"/><path d="M2 12h20M4 7h16M4 17h16"/></g></svg>
      www.karlvostermortgages.com
    </li>
    <li class="contacts__plain">
      <span class="icon icon--blank"></span>
      TPW Brokerage Lic. # 73918
    </li>
  </ul>

  <p class="agent-licence">Lic # M47105386</p>

  <div class="brokerage">
    <div class="brokerage__mark">
      <span class="brokerage__square"></span>
      <span class="brokerage__name">TPW</span>
    </div>
    <p class="brokerage__licence">License #73918</p>
  </div>
</section>

<section class="card card--back" aria-label="Business card back">
  <div class="back-mark">
    <span class="back-mark__square"></span>
    <span class="back-mark__name">TPW</span>
  </div>
</section>

</body>
</html>
```